Personal Injury Lawyer Billboard

I would like a design created featuring the image of the lawyer centered in the middle of the design.
To the left of the lawyer's image it should read "INJURED?"
To the right of the lawyer's image, it should read "CALL BRUNO!"
Under Call Bruno, include the phone number 318-555-0187.
At the bottom of the design include the lawyers information "Bruno Pemberly Accident & Injury Lawyers"
PLEASE REMOVED THE BACKGROUND IMAGERY OF THE PHOTO SUBMITTED. Also, the colors for this design should match the colors shown in the logo (navy, white and relective soft gold). Please use those color combinations in ways that best stand out.

```html
<!DOCTYPE html>
<html lang="en">
<head>
<meta charset="utf-8">
<title>Bruno Pemberly Accident &amp; Injury Lawyers – Billboard</title>
<link rel="stylesheet" href="https://fonts.googleapis.com/css2?family=Barlow+Condensed:wght@600;700&display=swap">
<style>
  :root {
    --paper: #ffffff;
    --navy: #0c1d47;
    --navy-deep: #0a1838;
    --navy-soft: #1a2f63;
    --white: #ffffff;
    --gold: #d2aa42;
    --gold-light: #e8cb6e;
  }
  html, body {
    margin: 0;
    padding: 0;
    width: 1200px;
    height: 1200px;
    overflow: hidden;
    background: var(--paper);
  }
  .canvas {
    position: relative;
    width: 1200px;
    height: 1200px;
    background: var(--paper);
    font-family: "Barlow Condensed", "Arial Narrow", sans-serif;
  }
  .billboard {
    position: absolute;
    left: 122px;
    top: 122px;
    width: 963px;
    height: 963px;
    background: radial-gradient(circle at 55% 40%, var(--navy) 0%, var(--navy-deep) 70%);
    overflow: hidden;
  }
  .lawyer-photo {
    position: absolute;
    left: 231px;
    top: 40px;
    width: 519px;
    height: 607px;
    background: linear-gradient(180deg, var(--navy-soft) 0%, var(--navy) 100%);
    border-radius: 240px 240px 0 0;
  }
  .headline {
    position: absolute;
    margin: 0;
    line-height: 1;
    font-weight: 700;
    color: var(--white);
    text-transform: uppercase;
    z-index: 2;
  }
  .headline--question {
    left: 34px;
    top: 22px;
    font-size: 98px;
  }
  .headline--call {
    right: 32px;
    top: 22px;
    font-size: 130px;
    text-align: right;
    line-height: 0.92;
  }
  .phone {
    position: absolute;
    left: 779px;
    top: 305px;
    margin: 0;
    font-size: 100px;
    font-weight: 700;
    line-height: 0.9;
    color: var(--gold);
    background: linear-gradient(180deg, var(--gold-light), var(--gold));
    -webkit-background-clip: text;
    background-clip: text;
    -webkit-text-fill-color: transparent;
    z-index: 2;
  }
  .phone span { display: block; }
  .firm {
    position: absolute;
    left: 95px;
    top: 650px;
    width: 774px;
    height: 273px;
    box-sizing: border-box;
    border: 3px solid var(--gold);
    background: var(--navy);
    display: flex;
    flex-direction: column;
    align-items: center;
    justify-content: center;
    gap: 14px;
    z-index: 3;
    color: var(--white);
    text-transform: uppercase;
    font-weight: 700;
    line-height: 1;
  }
  .firm__name {
    font-size: 112px;
    letter-spacing: 2px;
  }
  .firm__practice {
    font-size: 66px;
    letter-spacing: 1px;
  }
</style>
</head>
<body>
  <main class="canvas">
    <section class="billboard">
      <div class="lawyer-photo" role="img" aria-label="Portrait of the lawyer in a navy suit and green tie, smiling with a raised fist, background removed"></div>

      <h1 class="headline headline--question">Injured?</h1>
      <h2 class="headline headline--call">Call<br>Bruno!</h2>

      <p class="phone">
        <span>318-</span>
        <span>555-</span>
        <span>0187</span>
      </p>

      <div class="firm">
        <div class="firm__name">Bruno Pemberly</div>
        <div class="firm__practice">Accident &amp; Injury Lawyers</div>
      </div>
    </section>
  </main>
</body>
</html>
```